BRAVO Nutrition Mobile Application Layout

I am looking for professional grade app page layouts to use in my clickable prototype for an investor pitch.

B.R.A.V.O. is an acronym for Balanced Responsive Vitality Assessment Optimizer.

This app is a nutrition diet generation tool for the consumer (type in profile, diet is generated).

I am most interested in several pages consisting of:
- A landing/login page
- User profile page which will consist of a visual representation of adherence to the diet such as a pie chart, bar with percentage representing said adherence, etc.
- Profile settings page
- Blank general layout page (a standard template to be used with all pages in the application)

I would prefer greens, reds, and yellows in the design
The design should reflect health and nutrition
The design should have an "ease of use appearance"

Apps that are useful to look at are:
Trimwell Buddy
Nutrilogix
Grocevane

I have uploaded a "working" logo that I am using

I look forward to seeing your talents and appreciate your work in advance!

Target Market(s)

General population - health and wellness companies

Industry/Entity Type

Health And Wellness

Font styles to use
Serif
Sans Serif
Other font styles liked:
• Dealer's Choice

Colors
9ccb3b
f04a51
fbed22

Requirements
Must have
• - A landing/login page
• - User profile page which will consist of a visual representation of adherence to the diet such as a pie chart, bar with percentage representing said adherence, etc.
• - Profile settings page
• - Blank general layout page (a standard template to be used with all pages in the application)
• The design should reflect health and nutrition
• The design should have an "ease of use appearance"
Nice to have
• Incorporating the acronym spelled out.
• Common image in the background reflecting nutrition and health.

```html
<!DOCTYPE html>
<html lang="en">
<head>
<meta charset="utf-8">
<title>BRAVO – Welcome</title>
<link href="https://fonts.googleapis.com/css2?family=Nunito+Sans:wght@400;600;700;800;900&display=swap" rel="stylesheet">
<style>
  :root {
    --green: #84c52a;
    --white: #ffffff;
    --ink: #4a4f55;
    --night: #0d1a22;
    --warm-top: #7a4a32;
    --warm-mid: #5e3b2e;
    --logo-green: #6fae2a;
  }
  * { box-sizing: border-box; margin: 0; padding: 0; }
  html, body { width: 675px; height: 1200px; overflow: hidden; background: var(--night); }
  body { font-family: "Nunito Sans", Arial, sans-serif; color: var(--white); }

  .screen { position: relative; width: 675px; height: 1200px; overflow: hidden; }

  .backdrop {
    position: absolute; inset: 0;
    background: linear-gradient(180deg, var(--warm-top) 0%, var(--warm-mid) 55%, #3a2a26 78%, var(--night) 100%);
  }
  .shade {
    position: absolute; inset: 0;
    background: linear-gradient(180deg, rgba(13,26,34,.35) 0%, rgba(13,26,34,.35) 60%, rgba(13,26,34,.8) 82%, rgba(13,26,34,.95) 100%);
  }

  .status-bar {
    position: absolute; top: 0; left: 0; right: 0; height: 36px;
    display: flex; align-items: center; justify-content: space-between;
    padding: 0 10px; font-size: 21px; font-weight: 600;
  }
  .status-bar__left, .status-bar__right { display: flex; align-items: center; gap: 8px; width: 220px; }
  .status-bar__right { justify-content: flex-end; }
  .status-bar__time { font-weight: 700; }

  .brand {
    position: absolute; top: 229px; left: 0; right: 0;
    display: flex; flex-direction: column; align-items: center; text-align: center;
  }
  .brand__badge {
    width: 208px; height: 208px; border-radius: 50%; background: var(--white);
    display: flex; align-items: center; justify-content: center;
    color: var(--logo-green); font-weight: 800; font-size: 34px; letter-spacing: 2px;
  }
  .brand__name {
    margin-top: 52px; font-size: 68px; font-weight: 800; letter-spacing: 14px;
    line-height: 1; padding-left: 14px;
  }
  .brand__tagline {
    margin-top: 19px; font-size: 23px; font-weight: 800; letter-spacing: 4px;
    line-height: 36px; text-transform: uppercase; width: 560px;
  }

  .actions { position: absolute; left: 34px; right: 34px; top: 832px; display: flex; flex-direction: column; gap: 19px; }
  .button {
    height: 99px; border-radius: 50px; display: flex; align-items: center; justify-content: center; gap: 18px;
    font-size: 23px; letter-spacing: 3px; text-transform: uppercase; text-decoration: none;
  }
  .button--primary { background: var(--green); color: var(--white); font-weight: 800; }
  .button--secondary { background: var(--white); color: var(--ink); font-weight: 600; }
  .button__mark { width: 30px; height: 30px; background: var(--white); border-radius: 3px; }

  .login-prompt {
    position: absolute; left: 0; right: 0; top: 1104px; text-align: center;
    font-size: 27px; font-weight: 400;
  }
  .login-prompt a { color: var(--white); font-weight: 800; text-decoration: none; }
</style>
</head>
<body>
<main class="screen">
  <div class="backdrop" role="img" aria-label="Background photo of sliced citrus fruits"></div>
  <div class="shade"></div>

  <header class="status-bar">
    <div class="status-bar__left">
      <svg width="34" height="18" viewBox="0 0 34 18" aria-hidden="true" fill="#fff">
        <rect x="0" y="12" width="5" height="6" rx="1"/><rect x="8" y="9" width="5" height="9" rx="1"/>
        <rect x="16" y="5" width="5" height="13" rx="1"/><rect x="24" y="1" width="5" height="17" rx="1"/>
      </svg>
      <span>Signalo</span>
      <svg width="26" height="20" viewBox="0 0 26 20" aria-hidden="true" fill="none" stroke="#fff" stroke-width="3" stroke-linecap="round">
        <path d="M2 7a16 16 0 0 1 22 0"/><path d="M6 11a10 10 0 0 1 14 0"/><circle cx="13" cy="16" r="1.5" fill="#fff"/>
      </svg>
    </div>
    <span class="status-bar__time">9:41 AM</span>
    <div class="status-bar__right">
      <svg width="14" height="22" viewBox="0 0 14 22" aria-hidden="true" fill="none" stroke="#fff" stroke-width="2">
        <path d="M2 6l10 9-5 5V2l5 5-10 9"/>
      </svg>
      <span>100%</span>
      <svg width="46" height="22" viewBox="0 0 46 22" aria-hidden="true">
        <rect x="1" y="1" width="40" height="20" rx="4" fill="none" stroke="#fff" stroke-width="2"/>
        <rect x="4" y="4" width="34" height="14" rx="2" fill="#fff"/>
        <rect x="42" y="7" width="3" height="8" rx="1" fill="#fff"/>
      </svg>
    </div>
  </header>

  <section class="brand">
    <div class="brand__badge">BRAVO</div>
    <h1 class="brand__name">BRAVO</h1>
    <p class="brand__tagline">Balanced Responsive Vitality Assessment Optimizer</p>
  </section>

  <nav class="actions">
    <a class="button button--primary" href="#"><span class="button__mark"></span>Sign up with Linkora</a>
    <a class="button button--secondary" href="#">
      <svg width="38" height="28" viewBox="0 0 38 28" aria-hidden="true" fill="none" stroke="#4a4f55" stroke-width="2.5">
        <rect x="1.5" y="1.5" width="35" height="25" rx="1"/><path d="M1.5 2.5l17.5 13 17.5-13"/>
      </svg>
      Sign up with email
    </a>
  </nav>

  <p class="login-prompt">Already have an account? <a href="#">Log in</a></p>
</main>
</body>
</html>
```